High end wine label at Austrian Winery

We are a traditional winery in Austria in region Burgenland. We are looking for a relaunch of our current wine label for our [solstice] series. It's a high end wine series at an upper price range. At the moment we have just two kinds of the label, one white one for the white wines and one black one for the red wines. This is a series of wine, white, red, sweet, sparkling and a top wine categories. So we need the same label, but in 4 different ways to distinguish the wines plus the sparkling. Maybe in color, patterns, ... or something else. The label should be very simple, including our new logo. It's also possible to make one label but we can splitting two parts of the label. The size of the label does not matter, need not be the same as now. It's a bit higher than a normal bottle. Additionally we need a back label with wine description and the wine dates on it.

Target Market(s)

private consumers and restaurants, no retailers

Colors

Designer to choose colors to be used in the design.

Requirements
Must have
• simple label with 4 different categories (red, white, sweet, top) plus Frizzante label, new logo integrated, high end label. Just logo, grape variety and [solstice] as text on the front label as text
Nice to have
• It's just good, if there'sa possibility to have different colors of each grape variety (about 10 different), but all the same style. top Wines should have an extraordinary design, but familiar with the others
Should not have
• no cheap look

```html
<!DOCTYPE html>
<html lang="en">
<head>
<meta charset="utf-8">
<title>Halden Wine – [solstice] Series Labels</title>
<link rel="stylesheet" href="https://fonts.googleapis.com/css2?family=Michroma&family=Oswald:wght@400&display=swap">
<style>
  :root {
    --page: #ffffff;
    --label-paper: #f3f0e5;
    --label-paper-top: #ece5cc;
    --label-edge: #d9d4c4;
    --ink: #2b2b2b;
    --emboss: #e2ded1;
    --emboss-line: #d6d1c2;
    --seal-dark: #2d2a27;
    --accent-red: #b3242c;
    --accent-yellow: #c8b548;
    --accent-green: #8bb548;
    --accent-teal: #5fb1a3;
    --accent-taupe: #b1a591;
  }
  * { box-sizing: border-box; margin: 0; padding: 0; }
  html, body {
    width: 1200px; height: 969px; overflow: hidden;
    background: var(--page);
  }
  .label-range {
    position: relative;
    width: 1200px; height: 969px;
    display: flex; justify-content: center; align-items: center;
    gap: 38px;
  }
  .label {
    position: relative;
    width: 196px; height: 260px;
    background: var(--label-paper);
    box-shadow: inset 0 0 0 1px var(--label-edge);
    text-align: center;
    color: var(--ink);
  }
  .label--top { background: var(--label-paper-top); }
  .label__seal {
    position: absolute; left: 50%; top: 36px;
    width: 76px; height: 76px; transform: translateX(-50%);
  }
  .label__brand {
    position: absolute; left: 0; right: 0; top: 118px;
    font-family: "Michroma", sans-serif;
    font-size: 11.5px; letter-spacing: 1.6px; line-height: 1;
  }
  .label__tagline {
    position: absolute; left: 0; right: 0; top: 132px;
    font-family: "Oswald", sans-serif;
    font-size: 6px; letter-spacing: 1.4px; line-height: 1;
  }
  .label--top .label__brand { top: 125px; }
  .label--top .label__tagline { top: 139px; }
  .label__series {
    position: absolute; left: 0; right: 0; top: 198px;
    font-family: "Oswald", sans-serif;
    font-size: 12px; line-height: 1; letter-spacing: 0.2px;
  }
  .label--top .label__series { top: 190px; }
  .label__variety {
    position: absolute; left: 8px; right: 8px; top: 243px;
    font-family: "Michroma", sans-serif;
    font-size: 9px; letter-spacing: 2.4px; line-height: 1;
    font-weight: 400; white-space: nowrap;
  }
  .series--red { color: var(--accent-red); }
  .series--yellow { color: var(--accent-yellow); }
  .series--green { color: var(--accent-green); }
  .series--teal { color: var(--accent-teal); }
  .series--taupe { color: var(--accent-taupe); }
</style>
</head>
<body>
<main class="label-range">

  <section class="label">
    <svg class="label__seal" viewBox="0 0 76 76" aria-hidden="true">
      <circle cx="38" cy="38" r="36" fill="var(--emboss)" stroke="var(--emboss-line)" stroke-width="1"/>
    </svg>
    <p class="label__brand">HALDEN</p>
    <p class="label__tagline">BURGENLAND ESTATE</p>
    <p class="label__series series--red">[solstice]</p>
    <h2 class="label__variety">CABERNET</h2>
  </section>

  <section class="label">
    <svg class="label__seal" viewBox="0 0 76 76" aria-hidden="true">
      <circle cx="38" cy="38" r="36" fill="var(--emboss)" stroke="var(--emboss-line)" stroke-width="1"/>
    </svg>
    <p class="label__brand">HALDEN</p>
    <p class="label__tagline">BURGENLAND ESTATE</p>
    <p class="label__series series--yellow">[solstice]</p>
    <h2 class="label__variety">GRUNER VELTLINER</h2>
  </section>

  <section class="label">
    <svg class="label__seal" viewBox="0 0 76 76" aria-hidden="true">
      <circle cx="38" cy="38" r="36" fill="var(--emboss)" stroke="var(--emboss-line)" stroke-width="1"/>
    </svg>
    <p class="label__brand">HALDEN</p>
    <p class="label__tagline">BURGENLAND ESTATE</p>
    <p class="label__series series--green">[solstice]</p>
    <h2 class="label__variety">SPATLESE</h2>
  </section>

  <section class="label">
    <svg class="label__seal" viewBox="0 0 76 76" aria-hidden="true">
      <circle cx="38" cy="38" r="36" fill="var(--emboss)" stroke="var(--emboss-line)" stroke-width="1"/>
    </svg>
    <p class="label__brand">HALDEN</p>
    <p class="label__tagline">BURGENLAND ESTATE</p>
    <p class="label__series series--teal">[solstice]</p>
    <h2 class="label__variety">PINOT BLANC</h2>
  </section>

  <section class="label label--top">
    <svg class="label__seal" viewBox="0 0 76 76" aria-hidden="true">
      <circle cx="38" cy="38" r="37" fill="var(--seal-dark)"/>
    </svg>
    <p class="label__brand">HALDEN</p>
    <p class="label__tagline">BURGENLAND ESTATE</p>
    <p class="label__series series--taupe">[solstice]</p>
    <h2 class="label__variety">PINOT BLANC</h2>
  </section>

</main>
</body>
</html>
```